Tailbrook - eCommerce Design and Shopify Theme customisation

eCommerce Website Design - firstly with mockups then once we have chosen the design the successful designer will need to choose, purchase and customise a Shopify theme to match the design. We have a logo already designed and now want to create our web presence based on carrying up to 50 products on our website.
Target Market(s)
UK Pet Owners
Industry/Entity Type
Pet Shop
Requirements
Must have
- Design must be achievable using a customised Shopify theme - the successful designer will be responsible for the delivery of a working theme on our shopify website.
Should not have
- should not look cheap or have designs that aren't compatible or achievable with Shopify

```html
<!DOCTYPE html>
<html lang="en">
<head>
<meta charset="utf-8">
<title>Tailbrook – Pet Shop</title>
<link rel="stylesheet" href="https://fonts.googleapis.com/css2?family=Montserrat:wght@500;600;700&family=Open+Sans:wght@400&family=Poppins:wght@400;500&family=Syne:wght@600&display=swap">
<style>
  :root {
    --topbar-bg: #f6f6f6;
    --topbar-text: #777777;
    --ink: #1d1d1d;
    --white: #ffffff;
    --teal: #35b8a3;
    --yellow: #fdc114;
    --hero-red: #ad2f2e;
    --photo-light: #e9cfcf;
    --photo-mid: #c9595a;
  }
  * { box-sizing: border-box; margin: 0; padding: 0; }
  html, body { width: 1200px; height: 608px; overflow: hidden; background: var(--white); }
  body { position: relative; font-family: "Open Sans", sans-serif; }

  .topbar {
    position: absolute; left: 0; top: 0; width: 1200px; height: 30px;
    background: var(--topbar-bg); color: var(--topbar-text); font-size: 8.5px;
  }
  .topbar-item { position: absolute; top: 9px; display: flex; align-items: center; gap: 4px; }
  .topbar-item svg { fill: var(--topbar-text); }

  .header { position: absolute; left: 0; top: 30px; width: 1200px; height: 98px; }
  .brand {
    position: absolute; left: 214px; top: 34px; display: flex; align-items: center; gap: 8px;
    font-family: "Montserrat", sans-serif; font-weight: 600; font-size: 26px; color: var(--ink);
  }
  .brand-dot { width: 22px; height: 22px; border-radius: 50%; background: var(--yellow); }
  .search {
    position: absolute; left: 470px; top: 32px; width: 272px; height: 34px; border-radius: 17px;
    background: var(--teal); color: var(--white); font-size: 10px; padding: 11px 0 0 14px;
    font-family: "Montserrat", sans-serif; font-weight: 500;
  }
  .search-btn {
    position: absolute; right: 5px; top: 4px; width: 26px; height: 26px; border-radius: 50%;
    border: 1.5px solid var(--white); display: flex; align-items: center; justify-content: center;
  }
  .delivery {
    position: absolute; left: 791px; top: 45px; font-family: "Montserrat", sans-serif;
    font-weight: 600; font-size: 11px; letter-spacing: .3px; color: var(--ink);
  }

  .mainnav {
    position: absolute; left: 0; top: 128px; width: 1200px; height: 50px; background: var(--yellow);
    display: flex; justify-content: center; align-items: center; gap: 27px;
    font-family: "Montserrat", sans-serif; font-weight: 600; font-size: 11.5px; color: var(--white);
    letter-spacing: .4px; padding-right: 6px;
  }
  .mainnav .active { color: var(--ink); }
  .mainnav .sep { font-weight: 500; }
  .caret { display: inline-block; margin-left: 4px; border: 4px solid transparent; border-top-color: var(--white); border-bottom: 0; vertical-align: 2px; }

  .hero { position: absolute; left: 0; top: 178px; width: 1200px; height: 404px; background: var(--hero-red); overflow: hidden; }
  .hero-photo {
    position: absolute; left: 44px; top: 0; width: 660px; height: 404px;
    background: linear-gradient(90deg, var(--photo-mid) 0%, var(--photo-light) 40%, var(--photo-mid) 70%, var(--hero-red) 100%);
  }
  .hero-arrow {
    position: absolute; top: 160px; width: 38px; height: 38px; border-radius: 50%;
    background: var(--yellow); display: flex; align-items: center; justify-content: center;
  }
  .hero-arrow.prev { left: 49px; }
  .hero-arrow.next { left: 1147px; }
  .hero-title {
    position: absolute; left: 641px; top: 136px; font-family: "Syne", sans-serif; font-weight: 600;
    font-size: 44px; letter-spacing: 1px; color: var(--yellow); line-height: 1;
  }
  .hero-sub {
    position: absolute; left: 642px; top: 182px; font-family: "Poppins", sans-serif; font-weight: 400;
    font-size: 24px; letter-spacing: .5px; color: var(--white); line-height: 1;
  }
  .hero-cta {
    position: absolute; left: 636px; top: 237px; width: 132px; height: 34px; border-radius: 17px;
    background: var(--yellow); color: var(--ink); font-family: "Poppins", sans-serif; font-weight: 500;
    font-size: 12.5px; letter-spacing: .6px; display: flex; align-items: center; justify-content: center;
  }
</style>
</head>
<body>
  <div class="topbar">
    <div class="topbar-item" style="left:230px">
      <svg width="7" height="7" viewBox="0 0 24 24"><path d="M6.6 10.8a15 15 0 006.6 6.6l2.2-2.2c.3-.3.7-.4 1-.2 1.1.4 2.3.6 3.6.6.6 0 1 .4 1 1V20c0 .6-.4 1-1 1A17 17 0 013 4c0-.6.4-1 1-1h3.5c.6 0 1 .4 1 1 0 1.3.2 2.5.6 3.6.1.3 0 .7-.2 1z"/></svg>
      (00) 000 111 222
    </div>
    <div class="topbar-item" style="left:316px">
      <svg width="9" height="7" viewBox="0 0 24 18"><path d="M0 0h24v18H0zM2 2v1l10 7 10-7V2z"/></svg>
      hello@tailbrook.shop
    </div>
    <div class="topbar-item" style="left:823px">My Account</div>
    <div class="topbar-item" style="left:879px">USD
      <svg width="7" height="4" viewBox="0 0 8 4" style="margin-left:5px"><path d="M0 0h8L4 4z"/></svg>
    </div>
    <div class="topbar-item" style="left:927px">
      <svg width="11" height="10" viewBox="0 0 24 22"><path d="M0 0h4l1 3h19l-4 9H7l-1 2h16v2H3l3-5L3 2H0zM7 18a2 2 0 110 4 2 2 0 010-4zm12 0a2 2 0 110 4 2 2 0 010-4z"/></svg>
      Cart
    </div>
  </div>

  <header class="header">
    <div class="brand"><span class="brand-dot"></span>Tailbrook</div>
    <div class="search">Search..
      <span class="search-btn">
        <svg width="12" height="12" viewBox="0 0 24 24" fill="none" stroke="#fff" stroke-width="3"><circle cx="10" cy="10" r="6.5"/><path d="M15 15l5 5"/></svg>
      </span>
    </div>
    <div class="delivery">FREE DELIVERY ORDER OVER $100</div>
  </header>

  <nav class="mainnav">
    <span class="active">HOME</span><span class="sep">-</span>
    <span>DOG<i class="caret"></i></span><span class="sep">-</span>
    <span>CAT<i class="caret"></i></span><span class="sep">-</span>
    <span>ABOUT</span><span class="sep">-</span>
    <span>BLOG</span><span class="sep">-</span>
    <span>FAQS</span><span class="sep">-</span>
    <span>CONTACT</span>
  </nav>

  <section class="hero">
    <div class="hero-photo" role="img" aria-label="Puppy wearing a festive red and white coat among striped gift boxes"></div>
    <div class="hero-arrow prev">
      <svg width="12" height="12" viewBox="0 0 12 12" fill="none" stroke="#1d1d1d" stroke-width="2.2"><path d="M8 1L3 6l5 5"/></svg>
    </div>
    <div class="hero-arrow next">
      <svg width="12" height="12" viewBox="0 0 12 12" fill="none" stroke="#1d1d1d" stroke-width="2.2"><path d="M4 1l5 5-5 5"/></svg>
    </div>
    <h1 class="hero-title">COOL COATS</h1>
    <p class="hero-sub">for dogs</p>
    <div class="hero-cta">SHOP NOW</div>
  </section>
</body>
</html>
```